Redesign Of Flower Delivery Subscription Service Website

I need a revamped website of www.petal-tide.com

Please revamp current design using same content....

Target Market(s)

people who buy flowers. Brides, wedding planners, wedding photographer, married man, boyfriend, etc.

Industry/Entity Type

Florist

Number of Pages Required

5+ page

Colors

Designer to choose colors to be used in the design.

Requirements
Must have
• I need a revamped website of www.petal-tide.com
• Please revamp current design using same content....
Nice to have
Should not have

```html
<!DOCTYPE html>
<html lang="en">
<head>
<meta charset="utf-8">
<title>Petal Tide – Monthly Flowers Delivery</title>
<link rel="stylesheet" href="https://fonts.googleapis.com/css2?family=Montserrat:wght@400;500;600;700;800&family=Noto+Serif:wght@400&display=swap">
<style>
:root{
  --green:#8fd14f;
  --green-dark:#5c9e1f;
  --cream:#f8f3d4;
  --ink:#333333;
  --text:#555555;
  --muted:#6a6a6a;
  --white:#ffffff;
}
*{margin:0;padding:0;box-sizing:border-box}
html,body{width:1200px;height:2737px;overflow:hidden}
body{font-family:"Montserrat",sans-serif;color:var(--text);background:var(--white)}
.page{position:relative;width:1200px;height:2737px;overflow:hidden}
.abs{position:absolute}
.btn{position:absolute;background:var(--green);color:var(--white);font-weight:700;text-transform:uppercase;display:flex;align-items:center;justify-content:center;gap:8px}
.divider{display:block;height:3px;background:var(--green);border-radius:2px}

/* header + hero */
.hero{left:0;top:0;width:1200px;height:611px;background:linear-gradient(180deg,#f7f1cf 0%,#f2e9bd 70%,#e6dbb0 100%)}
.hero-table{left:0;top:520px;width:1200px;height:91px;background:linear-gradient(180deg,#b69b78,#7c654c)}
.hero-photo{left:660px;top:100px;width:540px;height:511px;background:linear-gradient(160deg,#6f8f3a 0%,#e9b83a 35%,#d9543e 60%,#b8386a 80%,#4e6a2a 100%)}
.logo{left:133px;top:30px;font-size:30px;font-weight:500;color:#555;letter-spacing:1px}
.logo small{display:block;font-size:9px;letter-spacing:.5px;margin-top:2px}
.logo .dot{display:inline-block;width:10px;height:10px;border-radius:50%;background:var(--green);margin-left:6px;vertical-align:middle}
.phone-top{left:818px;top:22px;font-size:14px;color:#444;display:flex;align-items:center;gap:8px;font-weight:500}
.buy{left:949px;top:13px;width:120px;height:34px;font-size:11px}
.nav{left:407px;top:63px;display:flex;gap:17px;font-size:12px;color:#444}
.nav span.active{border-bottom:2px solid var(--green);padding-bottom:4px}
.hero-title{left:147px;top:256px;font-size:48px;font-weight:800;color:#3a3a3a;line-height:58px}
.hero-sub{left:147px;top:319px;font-size:20px;font-weight:500;color:#3a3a3a}
.hero-price{left:147px;top:357px;font-size:20px;font-weight:500;color:#3a3a3a}
.hero-price b{color:var(--green-dark);font-weight:600}
.subscribe{left:151px;top:400px;width:159px;height:43px;font-size:13px;color:#2b3a1a}

/* features */
.features{left:0;top:611px;width:1200px;height:136px;background:var(--cream)}
.feature{top:35px;width:300px;display:flex;gap:22px}
.feature-icon{width:58px;height:62px;border-radius:8px;flex:none}
.feature h3{font-family:"Noto Serif",serif;font-weight:400;font-size:19px;color:#444;margin-bottom:6px}
.feature p{font-size:11.5px;line-height:19px;color:var(--muted)}
.feature-divider{top:35px;width:1px;height:70px;background:#e4dcb4}

/* cards */
.card{top:793px;width:298px}
.card-photo{width:298px;height:206px}
.card-body{position:relative;margin:-52px 13px 0;background:var(--white);padding:22px 14px 0;text-align:center}
.card-body.featured{border-top:4px solid var(--green)}
.card-body h3{font-size:13px;font-weight:700;color:#333;text-transform:uppercase;margin-bottom:14px}
.card-body p{font-size:11.5px;line-height:24px;color:var(--muted)}
.card-body .more{font-family:"Noto Serif",serif;font-size:12px;color:#333;margin-top:12px}
.card-body .divider{width:52px;margin:-6px auto 8px}

/* welcome */
.welcome{left:0;top:1225px;width:1200px;height:392px;background:var(--cream)}
.welcome h2{position:absolute;left:140px;top:60px;font-size:26px;font-weight:700;color:#333}
.welcome-text{position:absolute;left:143px;top:112px;width:420px;font-size:11.5px;line-height:21px;color:var(--muted)}
.welcome-text p{margin-bottom:20px}
.video{position:absolute;left:600px;top:38px;width:468px;height:310px;background:linear-gradient(135deg,#6f7d5c,#b83b2e 45%,#3f4b2a 75%,#9a9a86)}
.play{position:absolute;left:204px;top:125px}

/* email */
.email{left:0;top:1617px;width:1200px;height:323px;background:linear-gradient(90deg,#e2587a 0%,#f08b5d 22%,#e8c7c9 45%,#dfe7ef 62%,#e7edf3 100%)}
.email h2{position:absolute;left:610px;top:62px;width:390px;text-align:center;font-size:25px;font-weight:700;line-height:34px;color:#333}
.email p{position:absolute;left:610px;top:140px;width:390px;text-align:center;font-size:11.5px;line-height:20px;color:#333}
.email-form{position:absolute;left:610px;top:196px;width:391px;height:55px;border:1px solid #b9c3cc;background:rgba(255,255,255,.6)}
.email-form span{position:absolute;left:19px;top:20px;font-size:11px;color:#777}
.submit{left:255px;top:7px;width:130px;height:40px;font-size:11px}

/* seo */
.seo{left:0;top:1940px;width:1200px;height:438px}
.seo h2{position:absolute;left:0;top:60px;width:1200px;text-align:center;font-size:20px;font-weight:700;line-height:34px;color:#333}
.seo .divider{position:absolute;left:545px;top:147px;width:110px}
.seo-text{position:absolute;left:165px;top:178px;width:870px;text-align:center;font-size:11.5px;line-height:24px;color:#444}
.read-more{left:486px;top:343px;width:230px;height:44px;font-size:11px}

/* footer */
.footer{left:0;top:2378px;width:1200px;height:359px;background:linear-gradient(180deg,#252920,#1a1c15 70%,#2a1a1c)}
.footer h4{position:absolute;top:76px;font-size:13px;font-weight:600;color:var(--green);text-transform:uppercase}
.contact-row{position:absolute;left:150px;display:flex;gap:20px;font-size:12px;line-height:24px;color:#e8e8e8}
.contact-row svg{flex:none;margin-top:5px}
.services{position:absolute;left:527px;top:108px;font-size:12px;line-height:29px;color:#e8e8e8}
.social{position:absolute;left:787px;top:105px;display:flex;gap:13px}
.social span{width:23px;height:23px;display:block}
.footer-bar{position:absolute;left:0;top:305px;width:1200px;height:54px;border-top:1px solid rgba(255,255,255,.08)}
.copy{position:absolute;left:135px;top:20px;font-size:10px;color:#ddd}
.copy b{color:var(--green);font-weight:400}
.legal{position:absolute;right:136px;top:20px;font-size:10px;color:#ddd;display:flex;gap:16px}
</style>
</head>
<body>
<div class="page">

  <header class="abs hero">
    <div class="abs hero-table" role="img" aria-label="Weathered wooden tabletop"></div>
    <div class="abs hero-photo" role="img" aria-label="Bouquet of sunflowers, roses and tropical leaves"></div>
    <div class="abs logo">PETAL TIDE<span class="dot"></span><small>San Diego Flower Company</small></div>
    <div class="abs phone-top">
      <svg width="14" height="14" viewBox="0 0 24 24"><path fill="#444" d="M6.6 10.8a15 15 0 0 0 6.6 6.6l2.2-2.2c.3-.3.7-.4 1-.2 1.1.4 2.3.6 3.6.6.6 0 1 .4 1 1V20c0 .6-.4 1-1 1A17 17 0 0 1 3 4c0-.6.4-1 1-1h3.5c.6 0 1 .4 1 1 0 1.3.2 2.5.6 3.6.1.3 0 .7-.2 1z"/></svg>
      555-240-7318
    </div>
    <div class="btn buy">
      <svg width="14" height="13" viewBox="0 0 24 22"><path fill="#fff" d="M0 1h4l3 12h13l3-9H7"/><circle cx="9" cy="18" r="2" fill="#fff"/><circle cx="18" cy="18" r="2" fill="#fff"/></svg>
      Buy Now
    </div>
    <nav class="abs nav">
      <span class="active">Home</span><span>How it Works</span><span>Delivery Areas</span><span>Franchise</span><span>Blog</span><span>Free Flowers Monthly</span><span>Corporate Arrangements</span><span>Help</span>
    </nav>
    <h1 class="abs hero-title">ALWAYS FRESH</h1>
    <div class="abs hero-sub">Beautiful Flower Arrangements Delivered Monthly</div>
    <div class="abs hero-price">Now only <b>$69.95/MTH ($100 value)</b></div>
    <div class="btn subscribe">Subscribe Now</div>
  </header>

  <section class="abs features">
    <div class="abs feature" style="left:135px">
      <div class="feature-icon" role="img" aria-label="Tulips in a vase illustration" style="background:#f1c9b6"></div>
      <div><h3>Free Vase</h3><p>We're sure you would agree that beautiful flowers deserve.</p></div>
    </div>
    <div class="abs feature-divider" style="left:421px"></div>
    <div class="abs feature" style="left:453px">
      <div class="feature-icon" role="img" aria-label="Delivery scooter illustration" style="background:#b6e0d8"></div>
      <div><h3>Free Delivery</h3><p>Why pay for flower delivery when you can receive it for free.</p></div>
    </div>
    <div class="abs feature-divider" style="left:764px"></div>
    <div class="abs feature" style="left:803px">
      <div class="feature-icon" role="img" aria-label="Gift bag illustration" style="background:#f0d7b8"></div>
      <div><h3>Free Upgrade</h3><p>Are you a member of our monthly subscription service.</p></div>
    </div>
  </section>

  <article class="abs card" style="left:133px">
    <div class="card-photo" role="img" aria-label="Pastel bouquet with eucalyptus on white linen" style="background:linear-gradient(135deg,#e9ecee,#e9a99a 50%,#c9d1d2)"></div>
    <div class="card-body">
      <h3>Set It and Forget It</h3>
      <p>PetalTide is a "SET IT and FORGET IT" subscription based flower delivery service. For an Amazing price PetalTide will hand deliver a gorgeous arrangement directly to anyone you want every month without you having to worry about it.</p>
      <div class="more">Read More...</div>
    </div>
  </article>
  <article class="abs card" style="left:453px">
    <div class="card-photo" role="img" aria-label="Crate of mixed flowers carried by a florist" style="background:linear-gradient(135deg,#d8dde2,#e48b7a 45%,#8a9a55 70%,#b88c5a)"></div>
    <div class="card-body featured">
      <h3>But Never Forget Again</h3>
      <span class="divider"></span>
      <p>When setting up your account, you can choose exact delivery dates for the months that have special days such as your Anniversary, Birthday, Valentines Day and Mothers Day. You might forget but we won't, we have got ya covered!</p>
      <div class="more">Read More...</div>
    </div>
  </article>
  <article class="abs card" style="left:770px">
    <div class="card-photo" role="img" aria-label="Orange and red autumn arrangement" style="background:linear-gradient(135deg,#8f8a74,#d96a2a 45%,#b13a20 65%,#a5a89a)"></div>
    <div class="card-body">
      <h3>Making Someone's Day Better</h3>
      <p>Be the hero in that special someone's life each and every month.<br>It feels good to make a difference in your loved ones day.</p>
      <div class="more">Read More...</div>
    </div>
  </article>

  <section class="abs welcome">
    <h2>Welcome to Petal Tide</h2>
    <div class="welcome-text">
      <p>PetalTide is a SET IT and FORGET IT subscription based flower delivery service. For an amazing price PetalTide will hand deliver a gorgeous arrangement directly to anyone, anywhere you want, every month.</p>
      <p>When setting up your account, Petal Tide even lets you choose exact delivery dates for your Anniversary, Birthday, Valentine's and Mother's Day.</p>
      <p>Our referral program is pretty awesome too! Just refer 3 friends and each month your 3 friends pay to have flowers delivered, your flowers will be delivered free!</p>
    </div>
    <div class="video" role="img" aria-label="Video still of red dahlias in a metal bucket">
      <svg class="play" width="60" height="60" viewBox="0 0 60 60"><circle cx="30" cy="30" r="30" fill="#fff"/><path d="M24 19 L42 30 L24 41Z" fill="#8fd14f"/></svg>
    </div>
  </section>

  <section class="abs email" role="img" aria-label="Close-up of pink and orange roses on a pale blue background">
    <h2>Enter Your Email To<br>Receive A Free Upgrade</h2>
    <p>Flowers always make people better, happier, they are sunshine and medicine for the soul.</p>
    <div class="email-form">
      <span>Enter Your Email Address</span>
      <div class="btn submit">Submit
        <svg width="14" height="14" viewBox="0 0 24 24"><path d="M22 2 L2 10 L10 13 L13 22Z M10 13 L22 2" fill="none" stroke="#fff" stroke-width="1.8" stroke-linejoin="round"/></svg>
      </div>
    </div>
  </section>

  <section class="abs seo">
    <h2>Monthly Subscription Based Flower Delivery Service in<br>San Diego – CA by Our Florist Shop</h2>
    <span class="divider"></span>
    <p class="seo-text">Every moment of life could be cherished perfectly......IF you choose wisely. To make your day more treasured, remember that flowers are the smartest choice when delivered through our monthly PetalTide subscription based delivery service. Our online subscription-based flower delivery service can help you pamper, cherish and make an everlasting impression on the minds of your loved ones with a doorstep delivery of exquisitely hand-designed floral arrangements. Our online subscription service features both standard and personalized services to help you choose from an assortment of classic and contemporary floral arrangements. It is your chance to setup a weekly, monthly, or quarterly subscription, so we can deliver the most exotic collections of hand-decorated flowers that you and your loved ones will cherish.</p>
    <div class="btn read-more">Read More</div>
  </section>

  <footer class="abs footer" role="img" aria-label="Dark photo of red flowers in planters">
    <h4 style="left:145px">Contact Info</h4>
    <div class="contact-row" style="top:112px">
      <svg width="13" height="13" viewBox="0 0 24 24"><path d="M22 2 L2 11 L11 13 L13 22Z" fill="#fff"/></svg>
      <span>1480 Harbor Crest Way,<br>Lemon Grove, CA 91945</span>
    </div>
    <div class="contact-row" style="top:174px;font-size:13px;font-weight:600">
      <svg width="13" height="13" viewBox="0 0 24 24"><path fill="#fff" d="M6.6 10.8a15 15 0 0 0 6.6 6.6l2.2-2.2c.3-.3.7-.4 1-.2 1.1.4 2.3.6 3.6.6.6 0 1 .4 1 1V20c0 .6-.4 1-1 1A17 17 0 0 1 3 4c0-.6.4-1 1-1h3.5c.6 0 1 .4 1 1 0 1.3.2 2.5.6 3.6.1.3 0 .7-.2 1z"/></svg>
      <span>555-240-7318</span>
    </div>
    <div class="contact-row" style="top:214px">
      <svg width="13" height="11" viewBox="0 0 24 18"><rect width="24" height="18" rx="2" fill="#fff"/><path d="M1 2 L12 10 L23 2" fill="none" stroke="#1e2118" stroke-width="2"/></svg>
      <span>Email: support@petaltide-sd.com</span>
    </div>
    <h4 style="left:525px">More Services</h4>
    <div class="services">Corporate Arrangements<br>Hotel Arrangements<br>Events<br>Weddings</div>
    <h4 style="left:786px">Social Links</h4>
    <div class="social">
      <span style="background:#3b5998"></span><span style="background:#1da1f2"></span><span style="background:#dd4b39"></span><span style="background:#0077b5"></span>
    </div>
    <div class="footer-bar">
      <div class="copy"><b>Petal Tide - Monthly Flowers Delivery</b> Copyright 2018. All Rights Reserved.</div>
      <div class="legal"><span>Privacy Policy</span><span>|</span><span>Terms &amp; Conditions</span></div>
    </div>
  </footer>

</div>
</body>
</html>
```